Absoluter Profi, mit sehr wenigen Vorgaben und Anhaltspunkten ein Design gezaubert was uns umgehauen hat. Dieser Designer weiß was er tut. Zügig reagiert, pünktlich abgeliefert, qualitativ einwandfrei.
Zielgruppe
Wir sind eine Bauunternehmung (Meisterbetrieb und Ingenieurbüro) welche Erd- Maurer- und Betonarbeiten anbietet. Unser Fokus liegt auf Professionalität und qualitativ einwandfreie Arbeit. Wir sind teuer aber die besten in dem was wir machen. Unsere Zielgruppe liegt bei Kunden welche eine qualitativ einwandfreie Arbeit erwarten und bewusst sind dass das auch Geld kostet. Unserem Kunden ist die Geldfrage immer zweitrangig und er legt viel mehr wert auf andere Faktoren: Qualität, Zuverlässigkeit, Qualifikation, Termineinhaltung etc. Es ist selbstverständlich das die Kunden meist vermögender sind.
Aufgabenstellung
Format: 340 x 175 cm
Was muss drauf:
- Logo
- Firmendaten:
Lindenfeldweg 8, 89079 Ulm
Telefon: +49 (0) 7305 - 4817265
Mobil: +49 (0) 176 - 52938407
E-Mail: korvatek@mailtorvo.de
- Zusätzliche Informationen: Es sollte irgendwo noch 'Bauunternehmung' stehen, es sollte etwas größer sein, unter Logo oder ähnlich, Es muss klar sein das wir eine Bauunternehmung sind. Zusätzlich dazu noch unsere Leistungen 'Neubau, Umbau, Anbau', nebeneinander oder übereinander ist euch überlassen.

```html
<!DOCTYPE html>
<html lang="de">
<head>
<meta charset="utf-8">
<title>Korvatek – Bauunternehmung Banner</title>
<link rel="stylesheet" href="https://fonts.googleapis.com/css2?family=Montserrat:wght@400&family=Poppins:wght@500;600&display=swap">
<style>
  :root {
    --backdrop: #dcdcdc;
    --band-dark: #2a2b2e;
    --band-light: #f3f3f3;
    --ink-dark: #2b2c2f;
    --ink-light: #f4f4f4;
  }
  * { margin: 0; padding: 0; box-sizing: border-box; }
  html, body {
    width: 1200px; height: 864px; overflow: hidden;
    background: var(--backdrop);
    font-family: "Poppins", sans-serif;
  }
  .banner {
    position: absolute; left: 20px; top: 142px;
    width: 1160px; height: 579px;
    display: flex; flex-direction: column;
  }
  .brand-band {
    height: 200px; background: var(--band-dark);
    display: flex; justify-content: center; align-items: flex-start;
    padding-top: 29px;
  }
  .brand {
    display: flex; align-items: flex-end; gap: 32px; height: 143px;
  }
  .brand-square { width: 143px; height: 143px; background: var(--ink-light); }
  .brand-text {
    display: flex; flex-direction: column; align-items: flex-end;
    color: var(--ink-light);
  }
  .brand-tagline {
    font-family: "Montserrat", sans-serif; font-weight: 400;
    font-size: 15.5px; letter-spacing: 0.5px; line-height: 1;
    margin-bottom: 4px;
  }
  .brand-name {
    font-family: "Poppins", sans-serif; font-weight: 600;
    font-size: 104px; line-height: 0.95; letter-spacing: -2px;
  }
  .service-band {
    height: 229px; background: var(--band-light); color: var(--ink-dark);
    text-align: center; text-transform: uppercase; font-weight: 600;
  }
  .headline {
    font-size: 89px; line-height: 1; letter-spacing: 1px;
    padding-top: 30px;
  }
  .services {
    font-size: 61px; line-height: 1; letter-spacing: 1.5px;
    padding-top: 32px;
  }
  .contact-band {
    height: 150px; background: var(--band-dark); color: var(--ink-light);
    position: relative; text-transform: uppercase; font-weight: 500;
    font-size: 30px; letter-spacing: 0.3px;
  }
  .contact-col {
    position: absolute; top: 28px;
    display: flex; flex-direction: column; gap: 20px; line-height: 36px;
  }
  .contact-col--left { right: 619px; text-align: right; }
  .contact-col--right { left: 618px; text-align: left; }
  .contact-divider {
    position: absolute; left: 579px; top: 30px;
    width: 2px; height: 91px; background: var(--ink-light);
  }
</style>
</head>
<body>
  <main class="banner">
    <header class="brand-band">
      <div class="brand">
        <div class="brand-square"></div>
        <div class="brand-text">
          <span class="brand-tagline">MEISTERBETRIEB &amp; INGENIEURBÜRO</span>
          <span class="brand-name">korvatek</span>
        </div>
      </div>
    </header>
    <section class="service-band">
      <h1 class="headline">Bauunternehmung</h1>
      <p class="services">Neubau – Umbau – Anbau</p>
    </section>
    <footer class="contact-band">
      <div class="contact-col contact-col--left">
        <span>Tel : +49 (0) 7305 - 4817265</span>
        <span>Lindenfeldweg 8, 89079 Ulm</span>
      </div>
      <div class="contact-divider"></div>
      <div class="contact-col contact-col--right">
        <span>Mobil: +49 (0) 176 - 52938407</span>
        <span>E-Mail: korvatek@mailtorvo.de</span>
      </div>
    </footer>
  </main>
</body>
</html>
```